Business Card Design

We need the business card for our new business based in St. Marys, we manufacture mainly bubble wraps. And we would like the design to use our company logo and also make it easy for people to understand right away we are bubble wrap manufacturer

Industry/Entity Type

Business

Contact Information for Business Card

Cushora Pty Ltd, 14 Harlow Lane St. Marys NSW 2760, Tel: 02 9715 4826, Fax: 9715 4839, Dale Omar, General Manager, Mobile :0427 351 604, dale.omar@cushora.com.au, Website: cushora.com.au

```html
<!DOCTYPE html>
<html lang="en">
<head>
<meta charset="utf-8">
<title>Cushora Pty Ltd – Business Card</title>
<link rel="stylesheet" href="https://fonts.googleapis.com/css2?family=Lato:wght@400;700;900&family=Libre+Baskerville:wght@700&display=swap">
<style>
  :root {
    --stage: #ffffff;
    --card-dark: #303030;
    --card-back-dark: #333333;
    --band-light: #f2f2f2;
    --band-edge: #222222;
    --ink-light: #ffffff;
    --ink-grey: #5a5b5d;
    --ink-soft: #8a8a8a;
    --accent-red: #b3262b;
    --rule: #d9d9d9;
  }
  * { margin: 0; padding: 0; box-sizing: border-box; }
  html, body { width: 1200px; height: 819px; overflow: hidden; background: var(--stage); }
  body { position: relative; font-family: "Lato", sans-serif; }

  .card { position: absolute; overflow: hidden; }

  /* Back of card */
  .card-back { left: 530px; top: 25px; width: 637px; height: 381px; background: var(--card-back-dark); }
  .card-back .brand-band {
    position: absolute; left: 0; top: 0; width: 100%; height: 140px;
    background: var(--band-light); border-bottom: 4px solid var(--band-edge);
  }
  .brand { position: absolute; left: 0; width: 100%; text-align: center; }
  .brand-mark { display: inline-flex; align-items: center; gap: 10px; }
  .brand-square { display: inline-block; background: var(--accent-red); }
  .brand-name { font-family: "Lato", sans-serif; font-weight: 900; line-height: 1; }
  .brand-tagline { display: block; font-weight: 400; text-transform: uppercase; }

  .card-back .brand { top: 52px; }
  .card-back .brand-square { width: 26px; height: 26px; }
  .card-back .brand-name { font-size: 44px; color: var(--ink-grey); letter-spacing: 1px; }
  .card-back .brand-tagline { margin-top: 10px; font-size: 11.5px; letter-spacing: 3px; color: var(--ink-soft); }

  .holder { position: absolute; left: 60px; top: 212px; width: 220px; text-align: center; color: var(--ink-light); }
  .holder-name { font-size: 37px; font-weight: 700; letter-spacing: 0.5px; line-height: 1; }
  .holder-role { margin-top: 9px; font-size: 13px; }

  .divider { position: absolute; left: 301px; top: 152px; width: 2px; height: 181px; background: var(--rule); }

  .address {
    position: absolute; left: 320px; top: 160px; color: var(--ink-light);
    font-family: "Libre Baskerville", serif; font-weight: 700; font-size: 15px; line-height: 19px;
  }
  .contacts { position: absolute; left: 326px; top: 213px; list-style: none; color: var(--ink-light); }
  .contacts li { display: flex; align-items: center; height: 23.7px; font-size: 13.5px; }
  .contacts svg { width: 12px; height: 12px; margin-right: 9px; fill: var(--ink-light); flex: none; }

  /* Front of card */
  .card-front { left: 31px; top: 367px; width: 698px; height: 419px; background: var(--card-dark); }
  .front-rule { position: absolute; left: 71px; width: 556px; height: 2px; background: var(--rule); }
  .front-rule.top { top: 105px; }
  .front-rule.bottom { top: 308px; }
  .card-front .brand { top: 145px; }
  .card-front .brand-mark { gap: 18px; }
  .card-front .brand-square { width: 50px; height: 50px; }
  .card-front .brand-name { font-size: 80px; color: var(--ink-light); letter-spacing: 2px; }
  .card-front .brand-tagline { margin-top: 22px; font-size: 17px; letter-spacing: 5.6px; color: var(--ink-light); }
</style>
</head>
<body>

<section class="card card-back" aria-label="Business card, back">
  <div class="brand-band">
    <div class="brand">
      <span class="brand-mark"><span class="brand-square"></span><span class="brand-name">CUSHORA</span></span>
      <span class="brand-tagline">Protective Packaging Solutions</span>
    </div>
  </div>

  <div class="holder">
    <p class="holder-name">DALE OMAR</p>
    <p class="holder-role">General Manager</p>
  </div>

  <div class="divider"></div>

  <p class="address">14 Harlow Lane St.<br>Marys NSW 2760</p>

  <ul class="contacts">
    <li><svg viewBox="0 0 16 16" aria-label="Phone"><path d="M1 6c0-2 3-4 7-4s7 2 7 4l-3 1-1-2H5L4 7zM3 8l2-2h6l2 2v6H3zm5 1.5a2 2 0 100 4 2 2 0 000-4z"/></svg>02 9715 4826</li>
    <li><svg viewBox="0 0 16 16" aria-label="Fax"><path d="M8 0a8 8 0 110 16A8 8 0 018 0zm0 1.6a6.4 6.4 0 100 12.8A6.4 6.4 0 008 1.6zM5 4h6v8H5zm1.3 1.3v1.4h3.4V5.3zm0 2.7v1h3.4V8zm0 2v1h3.4v-1z"/></svg>9715 4839</li>
    <li><svg viewBox="0 0 16 16" aria-label="Mobile"><path d="M4 1h8v2H4zM2 4h12v11H2zm2 2v2h8V6zm0 4v1.5h2V10zm3 0v1.5h2V10zm3 0v1.5h2V10zm-6 2.5V14h2v-1.5zm3 0V14h2v-1.5zm3 0V14h2v-1.5z"/></svg>0427 351 604</li>
    <li><svg viewBox="0 0 16 16" aria-label="Email"><path d="M1 2h14v12H1zm2 2v1l5 3.5L13 5V4zm0 2.6V12h10V6.6L8 10z"/></svg>dale.omar@cushora.com.au</li>
    <li><svg viewBox="0 0 16 16" aria-label="Website"><path d="M8 0a8 8 0 110 16A8 8 0 018 0zM6.2 1.6A6.5 6.5 0 001.6 7.2h2.9c.1-2 .7-4 1.7-5.6zm3.6 0c1 1.6 1.6 3.6 1.7 5.6h2.9a6.5 6.5 0 00-4.6-5.6zM8 1.8C7 3.3 6.1 5.2 6 7.2h4C9.9 5.2 9 3.3 8 1.8zM1.6 8.8a6.5 6.5 0 004.6 5.6c-1-1.6-1.6-3.6-1.7-5.6zm4.4 0c.1 2 1 3.9 2 5.4 1-1.5 1.9-3.4 2-5.4zm5.5 0c-.1 2-.7 4-1.7 5.6a6.5 6.5 0 004.6-5.6z"/></svg>cushora.com.au</li>
  </ul>
</section>

<section class="card card-front" aria-label="Business card, front">
  <div class="front-rule top"></div>
  <div class="brand">
    <span class="brand-mark"><span class="brand-square"></span><span class="brand-name">CUSHORA</span></span>
    <span class="brand-tagline">Protective Packaging Solutions</span>
  </div>
  <div class="front-rule bottom"></div>
</section>

</body>
</html>
```